Shopping Mall Advertisement (Print)

Ridgeway Federal Credit Union is looking to create an Automobile Loan Ad. This ad is part of an ongoing campaign, so it must incorporate the box/art work “One Rate 1.99% We Promise.” We hope to encompass a Family/Car/Animals/Fun/Motif (not necessarily all of these in one ad – just listing ideas) that can be used for all seasons of the year. Additional requirements needed on the ad are RWY FCU logo, our web address for this ad ([login to view URL]) and the automobile terms (New, Used, Refinanced. Any Model Year, Any Term up to 7 years, One Rate for All Approved Applicants). Attached is our current ad – but would like to move away from the Muscle Car Motif. Required Logo and Rate Box that are attached do not need to be close to each other.

*** We are NOT looking for another MUSCLE CAR/CAR focused ad. Should be Family/Saving Money/Community/Fun. No QTC logo as shown from our old ad. ******* Thanks!

The advertisement will need to be a 300 DPI TIFF file measuring 23.5” W x 34.5” H (viewable area 22”W x 33”H and Copy Area = 21”W x 32”H) .

Additional requirements needed on the ad are RWY FCU logo (attached), the One Rate We Promise image, our web address ([login to view URL]) and the automobile loan terms (New, Used, Refinanced. Any Model Year, Any Term up to 7 years, One Rate for All Approved Applicants).

The Ad will need to be designed in either Adobe Illustrator or Photoshop CC (or lower).
A layered file with all supporting fonts and images must be provided to us upon awarding prize.

```html
<!DOCTYPE html>
<html lang="en">
<head>
<meta charset="utf-8">
<title>Ridgeway Federal Credit Union – Auto Loan Poster</title>
<link rel="stylesheet" href="https://fonts.googleapis.com/css2?family=Montserrat:wght@500;700;800&family=Black+Ops+One&display=swap">
<style>
  :root {
    --page-bg: #eceae7;
    --sun-yellow: #ffc61a;
    --sun-ray: #ffd54d;
    --asphalt: #3a3a3c;
    --stripe-white: #ffffff;
    --promo-red: #e3202a;
    --ink: #1e1e1e;
    --photo-light: #d9d9d6;
    --photo-dark: #8f8f8c;
  }
  * { box-sizing: border-box; margin: 0; padding: 0; }
  html, body { width: 1200px; height: 960px; overflow: hidden; }
  body {
    background: var(--page-bg);
    font-family: "Montserrat", Arial, sans-serif;
    position: relative;
  }
  .poster {
    position: absolute;
    left: 295px;
    top: 30px;
    width: 610px;
    height: 900px;
    overflow: hidden;
    background:
      repeating-conic-gradient(from 0deg at 300px 420px,
        var(--sun-yellow) 0deg 8deg, var(--sun-ray) 8deg 16deg);
  }
  .poster__shapes { position: absolute; inset: 0; }
  .brand {
    position: absolute;
    color: var(--stripe-white);
    font-weight: 700;
    line-height: 1.1;
    display: flex;
    align-items: center;
    gap: 8px;
  }
  .brand__dot {
    width: 12px; height: 12px; border-radius: 50%;
    background: var(--stripe-white);
    flex: none;
  }
  .brand--top { left: 22px; top: 46px; font-size: 15px; width: 170px; }
  .brand--bottom { left: 22px; top: 836px; font-size: 11px; width: 130px; }
  .rate-stamp {
    position: absolute;
    left: 208px;
    top: 196px;
    width: 160px;
    padding: 8px 6px;
    border: 5px solid var(--ink);
    outline: 2px solid var(--ink);
    outline-offset: 3px;
    transform: rotate(-9deg);
    font-family: "Black Ops One", "Arial Black", sans-serif;
    color: var(--ink);
    text-align: center;
    line-height: 1;
  }
  .rate-stamp__line { display: block; font-size: 24px; }
  .rate-stamp__rate { display: block; font-size: 42px; margin: 2px 0; }
  .rate-stamp__rate small { font-size: 18px; }
  .hero-photo {
    position: absolute;
    left: 23px;
    top: 344px;
    width: 545px;
    height: 322px;
    border-radius: 40px 40px 20px 20px;
    background: radial-gradient(ellipse at 35% 45%, var(--photo-light), var(--photo-dark) 85%);
  }
  .loan-terms {
    position: absolute;
    left: 0;
    top: 696px;
    width: 610px;
    text-align: center;
  }
  .loan-terms__types {
    color: var(--promo-red);
    font-weight: 800;
    font-size: 27px;
    letter-spacing: 0.5px;
  }
  .loan-terms__list {
    list-style: none;
    margin-top: 12px;
    font-weight: 700;
    font-size: 18px;
  }
  .loan-terms__list li { margin-bottom: 10px; }
  .bullet { color: var(--promo-red); margin-right: 6px; }
  .on-dark { color: var(--stripe-white); }
  .on-yellow { color: var(--ink); }
  .rate-highlight { color: var(--promo-red); font-weight: 800; font-size: 22px; }
  .web-address {
    position: absolute;
    right: 30px;
    top: 856px;
    color: var(--promo-red);
    font-weight: 800;
    font-size: 22px;
  }
</style>
</head>
<body>
  <main class="poster">
    <svg class="poster__shapes" viewBox="0 0 610 900" width="610" height="900" aria-hidden="true">
      <polygon fill="var(--asphalt)" points="470,0 610,0 610,210 440,470 370,470"/>
      <polygon fill="var(--stripe-white)" points="560,0 575,0 420,470 405,470"/>
      <polygon fill="var(--asphalt)" points="0,600 360,630 540,460 590,460 420,900 0,900"/>
      <polygon fill="var(--stripe-white)" points="610,420 610,440 455,900 430,900"/>
      <polygon fill="var(--sun-yellow)" points="0,880 0,840 300,700 320,712"/>
    </svg>

    <div class="brand brand--top"><span class="brand__dot"></span>Ridgeway Federal Credit Union</div>

    <div class="rate-stamp">
      <span class="rate-stamp__line">ONE RATE</span>
      <span class="rate-stamp__rate">1.99<small>%</small></span>
      <span class="rate-stamp__line">WE PROMISE</span>
    </div>

    <div class="hero-photo" role="img" aria-label="Silver SUV with a smiling family of three standing beside it"></div>

    <section class="loan-terms">
      <h2 class="loan-terms__types">NEW • USED • REFINANCED</h2>
      <ul class="loan-terms__list">
        <li><span class="bullet">●</span><span class="on-dark">ANY YEAR MODEL</span>&nbsp;&nbsp;&nbsp;<span class="bullet">●</span><span class="on-yellow">ANY TERM UPTO 7 YEARS</span></li>
        <li><span class="bullet">●</span><span class="on-dark">One Rate </span><span class="rate-highlight">1.99%</span><span class="on-yellow"> for All Approved Applicants</span></li>
      </ul>
    </section>

    <div class="brand brand--bottom"><span class="brand__dot"></span>Ridgeway Federal Credit Union</div>
    <div class="web-address">rwyfcu.org</div>
  </main>
</body>
</html>
```